'The Silent Ash of the Willow Lanterns' novel: book cover design (inc back & side)

My novel is called "The Silent Ash of the Willow Lanterns" and the subtitle is "A fallen sergeant defies the syndicate"
The book's description is:
"In December 1945 Kenji Morioka, an Crescent Guard officer, returns to war torn Osaka. He is a rare survivor from the Marrow Ridge campaign. Japan is in a wretched state, flattened by intensive bombing. Starvation and homelessness are rampant. Branded a defeated soldier, survivors treat him as an outcast. Penniless, he sleeps rough.
Amidst the city’s ruins and chaos, Black Markets explode. Some traders hawk goods looted from military stock piles. Others sell contraband sourced from racketeers in the occupation authorities. Yakuza gangs control the Black Markets, bribing police and city officials who turn a blind eye.
Morioka’s former Corporal runs a stall in the Kasuzawa Night Bazaar. Shaken down by the mob, he pleads for help. Can Morioka help? Will Morioka rediscover his once proud and invincible Samurai spirit?
The Silent Ash of the Willow Lanterns is a novel based on eye witness accounts and news reports.
Postwar Japan was a time when the weak were meat; the strong eat. "
The book design should apply for front, back and side. It will be an ePub and also printed version. The design should also work as a impactful thumbnail.
I need a designer who has interest or knowledge of Japan, where I live. Aspect ratio of 1.6 for the cover, size to 4500 pixels on the longest side.
I will supply the author's name later
Target Market(s)
Historical fiction readers; people interested in Japan & Japanese history; crime
Requirements
Must have
- An impactful cover design that works on printed, e-pub and also Quillora thumbnail. The design must be for front, back and side
- (Impactful = attractive, high standout, intrigues reader to buy the book)
Nice to have
- I have attached some imagery of post war Japan, the era when the novel is set.
- Note: the hero of the story is the defeated solider, not the Yakuza
Should not have
- stock image photos

```html
<!DOCTYPE html>
<html lang="en">
<head>
<meta charset="utf-8">
<title>The Silent Ash of the Willow Lanterns — Cover</title>
<link rel="stylesheet" href="https://fonts.googleapis.com/css2?family=Special+Elite&family=Open+Sans:wght@600;700&display=swap">
<style>
  :root {
    --stage: #dfe1e3;
    --front-ink: #2a2a2b;
    --front-edge: #2f86cf;
    --title-white: #f2f2f2;
    --back-edge: #3a3a3c;
    --back-deep: #1f6fa6;
    --back-light: #6fb4d8;
    --back-text: #1d1f22;
    --spine-ink: #2e2e30;
  }
  * { box-sizing: border-box; margin: 0; padding: 0; }
  html, body {
    width: 1200px; height: 900px; overflow: hidden;
    background: var(--stage);
  }
  .spread {
    position: relative; width: 1200px; height: 900px;
    display: flex; justify-content: center; align-items: center; gap: 36px;
  }
  .cover {
    position: relative; width: 330px; height: 528px; overflow: hidden;
    flex: none;
    box-shadow: 0 18px 40px rgba(0,0,0,0.18);
  }
  /* Front cover */
  .cover--front { background: var(--front-edge); padding: 6px; }
  .front-panel {
    position: relative; width: 100%; height: 100%; overflow: hidden;
    background-color: var(--front-ink);
    background-image:
      repeating-linear-gradient(0deg, rgba(255,255,255,0.025) 0 1px, transparent 1px 3px),
      repeating-linear-gradient(90deg, rgba(0,0,0,0.08) 0 1px, transparent 1px 3px);
  }
  .title-block {
    position: absolute; left: 29px; top: 205px; width: 260px;
    transform: rotate(-20deg); transform-origin: center center;
    white-space: nowrap;
  }
  .book-title {
    font-family: "Special Elite", "Courier New", serif;
    font-weight: 400; color: var(--title-white);
    font-size: 38px; line-height: 1.05; letter-spacing: -1px;
    text-shadow: 0 0 1px rgba(255,255,255,0.5);
  }
  .book-title span { display: block; }
  .book-title .l2 { padding-left: 20px; }
  .book-title .l3 { padding-left: 44px; }
  .book-title .l4 { padding-left: 66px; }
  .book-subtitle {
    font-family: "Open Sans", sans-serif; font-weight: 600;
    font-size: 9px; color: var(--title-white);
    margin: 4px 0 0 70px;
  }
  /* Spine */
  .spine {
    position: relative; width: 34px; height: 528px; flex: none;
    background: linear-gradient(90deg, var(--front-edge) 0 4px, var(--spine-ink) 4px calc(100% - 4px), var(--back-edge) calc(100% - 4px));
    box-shadow: 0 18px 40px rgba(0,0,0,0.18);
  }
  /* Back cover */
  .cover--back { background: var(--back-edge); padding: 6px; }
  .back-panel {
    position: relative; width: 100%; height: 100%;
    background: linear-gradient(160deg, var(--back-light) 0%, var(--back-deep) 45%, var(--back-light) 100%);
    display: flex; flex-direction: column; align-items: center;
  }
  .back-blurb {
    margin-top: 190px; width: 260px; text-align: center;
    font-family: "Open Sans", sans-serif; font-weight: 700;
    font-size: 8.5px; line-height: 1.3; color: var(--back-text);
  }
  .back-imprint {
    position: absolute; bottom: 26px; left: 0; right: 0; text-align: center;
    font-family: "Open Sans", sans-serif; font-weight: 700;
    font-size: 8.5px; color: var(--back-text);
  }
</style>
</head>
<body>
<main class="spread">
  <section class="cover cover--front">
    <div class="front-panel">
      <div class="title-block">
        <h1 class="book-title">
          <span class="l1">The Silent</span>
          <span class="l2">Ash of the</span>
          <span class="l3">Willow</span>
          <span class="l4">Lanterns</span>
        </h1>
        <p class="book-subtitle">A fallen sergeant defies the syndicate</p>
      </div>
    </div>
  </section>
  <section class="spine" aria-label="Spine"></section>
  <section class="cover cover--back">
    <div class="back-panel">
      <p class="back-blurb">The Silent Ash of the Willow Lanterns is a novel based on eye witness accounts and news reports</p>
      <p class="back-imprint">123 Lorem</p>
    </div>
  </section>
</main>
</body>
</html>
```